Need Flyer for Our Real estate Agency

Need to run General Campaign for our agency with Start of New Year as our theme ..Must have an agent's picture on the DL..
Address:
9 / 386Barwin rd, Truganina VIC 3029
Ph:03 9142 7305
email:info@koridanrealestate.example.au
www.koridanrealestate.example.au
Something like as attached picture..
Target Market(s)
Home Buyers
Industry/Entity Type
Real Estate Agent
Requirements
Must have
- Our Logo Colours

```html
<!DOCTYPE html>
<html lang="en">
<head>
<meta charset="utf-8">
<title>Koridan Real Estate – DL Flyer</title>
<link rel="stylesheet" href="https://fonts.googleapis.com/css2?family=Anton&family=Roboto+Condensed:wght@700&family=Raleway:wght@300;400&display=swap">
<style>
  :root {
    --navy: #1b2656;
    --navy-deep: #141c45;
    --red: #b01f2e;
    --white: #ffffff;
    --text-soft: #e3e6f0;
    --stage: #e8e9ed;
  }
  * { box-sizing: border-box; margin: 0; padding: 0; }
  html, body {
    width: 1200px; height: 900px; overflow: hidden;
    background: var(--stage);
  }
  .flyer {
    position: absolute; left: 62px; top: 207px;
    width: 1075px; height: 485px;
    background: radial-gradient(ellipse at 30% 40%, var(--navy) 0%, var(--navy-deep) 100%);
    overflow: hidden;
    box-shadow: 0 6px 18px rgba(0,0,0,.18);
  }
  .flyer-shapes { position: absolute; inset: 0; }
  .brand {
    position: absolute; left: 50px; top: 64px; width: 122px;
    text-align: center; color: var(--white);
    font-family: "Raleway", sans-serif; font-weight: 400;
  }
  .brand-name { display: block; font-size: 25px; letter-spacing: 2px; }
  .brand-sub { display: block; font-size: 7px; letter-spacing: 2px; margin-top: 2px;
    border-top: 1px solid var(--white); border-bottom: 1px solid var(--white); padding: 1px 0; }
  .headline { position: absolute; left: 50px; top: 124px; }
  .headline-main {
    display: block; font-family: "Anton", sans-serif; color: var(--white);
    font-size: 98px; line-height: 1; letter-spacing: 1px;
  }
  .headline-accent {
    display: block; font-family: "Raleway", sans-serif; font-weight: 300;
    color: var(--red); font-size: 40px; line-height: 1; margin-top: -2px;
  }
  .headline-question {
    display: block; font-family: "Roboto Condensed", sans-serif; font-weight: 700;
    color: var(--white); font-size: 60px; line-height: 1.05;
  }
  .divider {
    position: absolute; left: 52px; top: 343px; width: 438px; height: 2px;
    background: var(--white);
  }
  .offer {
    position: absolute; left: 50px; top: 372px;
    font-family: "Raleway", sans-serif; font-weight: 300;
    color: var(--text-soft); font-size: 17px;
  }
  .contact-list {
    position: absolute; left: 50px; top: 422px; width: 500px;
    list-style: none; display: grid; grid-template-columns: 290px 210px; row-gap: 10px;
    font-family: "Raleway", sans-serif; font-weight: 400; font-size: 12.5px; color: var(--text-soft);
  }
  .contact-item { display: flex; align-items: center; gap: 7px; }
  .contact-icon { width: 8px; height: 8px; flex: none; }
</style>
</head>
<body>
  <main class="flyer">
    <svg class="flyer-shapes" viewBox="0 0 1075 485" width="1075" height="485">
      <defs>
        <linearGradient id="house-photo-tone" x1="0" y1="0" x2="0" y2="1">
          <stop offset="0" stop-color="#7fb4e6"/>
          <stop offset="0.45" stop-color="#b8cfe0"/>
          <stop offset="0.6" stop-color="#a4553f"/>
          <stop offset="0.85" stop-color="#6f8a4e"/>
          <stop offset="1" stop-color="#cfc8bb"/>
        </linearGradient>
        <linearGradient id="agent-photo-tone" x1="0" y1="0" x2="0" y2="1">
          <stop offset="0" stop-color="#f4f4f6"/>
          <stop offset="0.55" stop-color="#d9d2cf"/>
          <stop offset="1" stop-color="#2c5fb8"/>
        </linearGradient>
      </defs>
      <polygon class="chevron-red-outer" fill="#b01f2e" points="662,0 1075,0 1075,485 700,485 440,230"/>
      <polygon class="chevron-white" fill="#ffffff" points="690,0 1075,0 1075,485 740,485 478,230"/>
      <polygon class="chevron-red-inner" fill="#b01f2e" points="718,0 1075,0 1075,485 790,485 540,228"/>
      <polygon class="chevron-white-thin" fill="#ffffff" points="738,0 1075,0 1075,485 822,485 582,222"/>
      <polygon class="house-photo" role="img" aria-label="Photo of a two-storey red brick home with a balcony and front fence"
               fill="url(#house-photo-tone)" points="745,0 1075,0 1075,485 832,485 596,222"/>
      <circle cx="759" cy="367" r="92" fill="#ffffff"/>
      <circle cx="759" cy="367" r="84" fill="none" stroke="#b01f2e" stroke-width="1" opacity=".0"/>
      <circle class="agent-photo" role="img" aria-label="Portrait photo of the agency's agent" cx="759" cy="367" r="84" fill="url(#agent-photo-tone)"/>
    </svg>

    <div class="brand">
      <span class="brand-name">KORIDAN</span>
      <span class="brand-sub">REAL ESTATE</span>
    </div>

    <h1 class="headline">
      <span class="headline-main">CURIOUS</span>
      <span class="headline-accent">to know what your</span>
      <span class="headline-question">Home is Worth?</span>
    </h1>

    <div class="divider"></div>
    <p class="offer">Contact us to arrange your free market appraisal</p>

    <ul class="contact-list">
      <li class="contact-item">
        <svg class="contact-icon" viewBox="0 0 8 8"><g fill="#c8202f"><rect width="3.5" height="3.5"/><rect x="4.5" width="3.5" height="3.5"/><rect y="4.5" width="3.5" height="3.5"/><rect x="4.5" y="4.5" width="3.5" height="3.5"/></g></svg>
        9 / 386Barwin rd, Truganina VIC 3029
      </li>
      <li class="contact-item">
        <svg class="contact-icon" viewBox="0 0 8 8"><g fill="#c8202f"><rect width="3.5" height="3.5"/><rect x="4.5" width="3.5" height="3.5"/><rect y="4.5" width="3.5" height="3.5"/><rect x="4.5" y="4.5" width="3.5" height="3.5"/></g></svg>
        info@koridanrealestate.example.au
      </li>
      <li class="contact-item">
        <svg class="contact-icon" viewBox="0 0 8 8"><g fill="#c8202f"><rect width="3.5" height="3.5"/><rect x="4.5" width="3.5" height="3.5"/><rect y="4.5" width="3.5" height="3.5"/><rect x="4.5" y="4.5" width="3.5" height="3.5"/></g></svg>
        03 9142 7305
      </li>
      <li class="contact-item">
        <svg class="contact-icon" viewBox="0 0 8 8"><g fill="#c8202f"><rect width="3.5" height="3.5"/><rect x="4.5" width="3.5" height="3.5"/><rect y="4.5" width="3.5" height="3.5"/><rect x="4.5" y="4.5" width="3.5" height="3.5"/></g></svg>
        www.koridanrealestate.example.au
      </li>
    </ul>
  </main>
</body>
</html>
```